A new presentation to our clients

we are a Real Estate agency, our website is www.dorelumia.com and it’s time to have a new, fashion and remarcable Business Card. we want to differentiate ourselves from other companies so we want a business card that differentiates us. we want the business card to impact our customers. in the competitive market that we have today, we have to be different and it is this difference that we seek

Target Market(s)

Real Estate Clients

Contact Information for Business Card

We search a totaly diferent card from the usual

Font styles to use
Sans Serif

Colors
e34197

Requirements
Must have
• Logo, adress, phone contact, e-mail, photo, and our website
Nice to have
• We would like to see a modern business card
Should not have
• Houses or building draws

```html
<!DOCTYPE html>
<html lang="en">
<head>
<meta charset="utf-8">
<title>Dore Lumia – Business Card</title>
<link href="https://fonts.googleapis.com/css2?family=Work+Sans:wght@400;500;600&display=swap" rel="stylesheet">
<style>
  :root {
    --bg: #1c1c1c;
    --card: #262626;
    --card-edge: #2f2f2f;
    --accent: #e3197e;
    --text: #f2f2f2;
    --photo-top: #d9d2c8;
    --photo-bottom: #2a2b33;
  }
  * { margin: 0; padding: 0; box-sizing: border-box; }
  html, body { width: 1200px; height: 900px; overflow: hidden; }
  body {
    background: var(--bg);
    font-family: "Work Sans", Arial, sans-serif;
    color: var(--text);
    position: relative;
  }
  .card {
    position: absolute;
    left: 250px;
    width: 700px;
    height: 400px;
    background: linear-gradient(135deg, var(--card) 0%, var(--card-edge) 100%);
    box-shadow: 0 10px 30px rgba(0,0,0,.5);
  }
  .card--front { top: 30px; display: flex; align-items: center; justify-content: center; }
  .card--back { top: 470px; }
  .brand-name {
    color: var(--accent);
    font-size: 68px;
    font-weight: 500;
    letter-spacing: 1px;
  }
  .portrait {
    position: absolute;
    left: 175px;
    top: 95px;
    width: 140px;
    height: 165px;
    border: 3px solid var(--accent);
    padding: 6px;
  }
  .portrait-fill {
    width: 100%;
    height: 100%;
    background: linear-gradient(180deg, var(--photo-top) 0%, #b9a48a 45%, var(--photo-bottom) 100%);
  }
  .divider {
    position: absolute;
    left: 352px;
    top: 85px;
    width: 3px;
    height: 185px;
    background: var(--accent);
  }
  .contact {
    position: absolute;
    left: 385px;
    top: 100px;
  }
  .person-name {
    color: var(--accent);
    font-size: 28px;
    font-weight: 500;
    letter-spacing: 1px;
    line-height: 1.05;
  }
  .person-role { font-size: 18px; margin-bottom: 14px; }
  .contact-list { list-style: none; }
  .contact-list li {
    display: flex;
    align-items: center;
    gap: 10px;
    font-size: 19px;
    line-height: 27px;
    letter-spacing: .5px;
  }
  .contact-list svg { width: 13px; height: 13px; flex: none; }
  .address {
    position: absolute;
    left: 95px;
    bottom: 42px;
    font-size: 20px;
    letter-spacing: .8px;
  }
</style>
</head>
<body>
  <section class="card card--front">
    <div class="brand-name">Dore Lumia</div>
  </section>

  <section class="card card--back">
    <div class="portrait"><div class="portrait-fill" role="img" aria-label="Portrait photo of the director"></div></div>
    <div class="divider"></div>
    <div class="contact">
      <div class="person-name">LENA MARSH</div>
      <div class="person-role">Director</div>
      <ul class="contact-list">
        <li>
          <svg viewBox="0 0 16 16"><path d="M4 1 L6.5 4.5 L5 6.5 C6 8.5 7.5 10 9.5 11 L11.5 9.5 L15 12 L13 15 C7 14 2 9 1 3 Z" fill="var(--accent)"/></svg>
          (+351) 210 480 215
        </li>
        <li>
          <svg viewBox="0 0 16 16"><rect x="4" y="1" width="8" height="4" fill="var(--accent)"/><rect x="1" y="6" width="14" height="6" rx="1" fill="var(--accent)"/><rect x="4" y="10" width="8" height="5" fill="var(--accent)"/></svg>
          (+351) 210 480 219
        </li>
        <li>
          <svg viewBox="0 0 16 16"><rect x="1.5" y="3.5" width="13" height="9" fill="none" stroke="var(--accent)" stroke-width="1.5"/><path d="M1.5 3.5 L8 9 L14.5 3.5" fill="none" stroke="var(--accent)" stroke-width="1.5"/></svg>
          geral@dorelumia.com
        </li>
        <li>
          <svg viewBox="0 0 16 16"><circle cx="8" cy="8" r="6.5" fill="none" stroke="var(--accent)" stroke-width="1.3"/><ellipse cx="8" cy="8" rx="3" ry="6.5" fill="none" stroke="var(--accent)" stroke-width="1.2"/><path d="M1.5 8 H14.5" stroke="var(--accent)" stroke-width="1.2"/></svg>
          www.dorelumia.com
        </li>
      </ul>
    </div>
    <div class="address">Rua das Acácias, 148 4410-052, Vila Nova de Gaia</div>
  </section>
</body>
</html>
```